Design some Business Cards for Bright Harbour Advisory

I'm looking for a business card.
Business name - Bright Harbour Advisory (logo attached)
Details:
Dane Whitlock
dane@homestepsupport.com.au
0491 273 518
I want it to look simple and professional

```html
<!DOCTYPE html>
<html lang="en">
<head>
<meta charset="utf-8">
<title>Bright Harbour Advisory – Business Cards</title>
<link href="https://fonts.googleapis.com/css2?family=Open+Sans:wght@400;600;700&display=swap" rel="stylesheet">
<style>
  :root {
    --backdrop: #3a3a3c;
    --card: #f7f7f5;
    --card-shade: #e9e9e6;
    --green: #9ccb63;
    --green-dark: #7fae48;
    --grey-line: #8e9092;
    --text-dark: #555a5e;
    --brand: #6d9a3c;
    --white: #ffffff;
  }
  * { box-sizing: border-box; margin: 0; padding: 0; }
  html, body { width: 1200px; height: 901px; overflow: hidden; }
  body {
    background: var(--backdrop);
    font-family: "Open Sans", Arial, sans-serif;
    position: relative;
  }
  .card {
    position: absolute;
    width: 520px;
    height: 300px;
    border-radius: 18px;
    background: linear-gradient(135deg, var(--white), var(--card) 60%, var(--card-shade));
    overflow: hidden;
  }
  .card--front { left: 60px; top: 300px; }
  .card--back { left: 620px; top: 300px; }

  .brand {
    display: flex;
    align-items: center;
    gap: 10px;
    color: var(--brand);
    font-weight: 700;
    font-size: 26px;
    letter-spacing: 0.5px;
  }
  .brand__mark {
    width: 16px; height: 16px;
    background: var(--brand);
  }
  .card--front .brand { position: absolute; left: 36px; top: 62px; }

  .band {
    position: absolute;
    left: 0; right: 0;
    top: 160px;
    height: 92px;
    background: var(--green);
    border-top: 4px solid var(--grey-line);
    border-bottom: 4px solid var(--grey-line);
    display: flex;
    align-items: center;
  }
  .band__person { width: 260px; padding-left: 36px; color: var(--white); }
  .band__name { font-size: 22px; font-weight: 600; }
  .band__title { font-size: 12px; margin-top: 2px; }
  .band__divider { width: 1px; height: 56px; background: rgba(255,255,255,0.6); }
  .contacts { list-style: none; padding-left: 24px; color: var(--white); font-size: 11.5px; }
  .contacts li { display: flex; align-items: center; gap: 8px; line-height: 20px; }
  .contacts svg { width: 12px; height: 12px; fill: var(--white); flex: none; }

  .back-pattern {
    position: absolute; inset: 0;
    background: linear-gradient(160deg, #fafaf8, #ececea);
  }
  .back-rule {
    position: absolute;
    left: 58px; top: 0; bottom: 0;
    width: 3px;
    background: var(--green-dark);
  }
  .back-web {
    position: absolute;
    left: 38px; top: 150px;
    transform: translate(-50%, -50%) rotate(-90deg);
    font-size: 11px;
    color: var(--text-dark);
    white-space: nowrap;
  }
  .card--back .brand { position: absolute; left: 120px; top: 130px; }
</style>
</head>
<body>
  <section class="card card--front" aria-label="Business card front">
    <div class="brand"><span class="brand__mark"></span>Bright Harbour Advisory</div>
    <div class="band">
      <div class="band__person">
        <div class="band__name">Dane Whitlock</div>
        <div class="band__title">Landscape Advisor</div>
      </div>
      <div class="band__divider"></div>
      <ul class="contacts">
        <li><svg viewBox="0 0 24 24"><path d="M6.6 10.8a15 15 0 0 0 6.6 6.6l2.2-2.2c.3-.3.7-.4 1-.2 1.1.4 2.3.6 3.6.6.6 0 1 .4 1 1V20c0 .6-.4 1-1 1A17 17 0 0 1 3 4c0-.6.4-1 1-1h3.5c.6 0 1 .4 1 1 0 1.3.2 2.5.6 3.6.1.3 0 .7-.2 1z"/></svg>0491 273 518</li>
        <li><svg viewBox="0 0 24 24"><path d="M2 5h20v14H2zm2 2v.5l8 5 8-5V7l-8 5z"/></svg>dane@homestepsupport.com.au</li>
        <li><svg viewBox="0 0 24 24"><circle cx="12" cy="12" r="10"/></svg>www.homestepsupport.com.au</li>
      </ul>
    </div>
  </section>

  <section class="card card--back" aria-label="Business card back">
    <div class="back-pattern" role="img" aria-label="Faint repeated brand pattern across the card background"></div>
    <div class="back-rule"></div>
    <div class="back-web">www.homestepsupport.com.au</div>
    <div class="brand"><span class="brand__mark"></span>Bright Harbour Advisory</div>
  </section>
</body>
</html>
```